Business Card Design and Basic Text Logo

We are looking for a business card design for an e-business company. Our business is the parent company of a few website businesses. The final logo and business card design will communicate a conservative but modern and expansive business

The Logo text is: 87Merchant
We would also like a basic text logo design for 87Merchant. The logo could also fill up the reverse side of the business card.

The colours we would like to use are:
White
Navy
Black

This is the text that will be added to the card:

Dean Colley
Business Development Manager

Phone: +61 417 658 294
Email: dean.colley@87merchant.com.au

Industry/Entity Type

Business

Logo Text

87Merchant

Logo styles of interest
Pictorial/Combination Logo
Requirements
Must have
• Modern and attractive design
Nice to have
• communicate a conservative but modern and expansive business
Should not have
• Should be too dull and plan
• But also should be overly colourful

```html
<!DOCTYPE html>
<html lang="en">
<head>
<meta charset="utf-8">
<title>87Merchant Business Card</title>
<link href="https://fonts.googleapis.com/css2?family=Open+Sans:ital,wght@0,400;0,600;0,700;1,400&display=swap" rel="stylesheet">
<style>
  :root {
    --backdrop: #e8e9ec;
    --card-white: #ffffff;
    --brand-blue: #1f78c8;
    --brand-navy: #2d5e9e;
    --slate-blue: #5d6c86;
    --charcoal: #3b3b3e;
    --ink: #1c1c20;
    --muted: #55575c;
  }
  * { box-sizing: border-box; margin: 0; padding: 0; }
  html, body { width: 1200px; height: 600px; overflow: hidden; }
  body {
    background: var(--backdrop);
    font-family: "Open Sans", Arial, sans-serif;
    position: relative;
  }
  .card {
    position: absolute;
    top: 145px;
    width: 540px;
    height: 310px;
    overflow: hidden;
    box-shadow: 0 6px 18px rgba(0,0,0,0.18);
  }
  .card-back { left: 40px; background: linear-gradient(100deg, var(--brand-navy) 0%, var(--slate-blue) 100%); }
  .card-front { left: 620px; background: var(--card-white); }

  .brand { display: flex; align-items: center; gap: 10px; position: absolute; }
  .brand-square { display: block; background: var(--brand-blue); }
  .brand-name { font-weight: 700; color: var(--brand-blue); letter-spacing: -0.5px; }

  .card-back .brand { left: 50%; top: 50%; transform: translate(-50%, -50%); gap: 14px; }
  .card-back .brand-square { width: 40px; height: 40px; background: var(--card-white); }
  .card-back .brand-name { font-size: 52px; color: var(--ink); }
  .card-back .website { position: absolute; left: 30px; bottom: 26px; color: var(--card-white); font-size: 15px; font-weight: 600; }

  .card-front .brand { left: 28px; top: 22px; }
  .card-front .brand-square { width: 22px; height: 22px; }
  .card-front .brand-name { font-size: 28px; }

  .swoosh { position: absolute; inset: 0; width: 100%; height: 100%; }

  .person { position: absolute; left: 50px; top: 88px; }
  .person-name { font-size: 21px; font-weight: 700; color: var(--ink); line-height: 1.1; }
  .person-name .surname { color: var(--brand-blue); }
  .person-title { font-size: 9px; font-style: italic; color: var(--muted); margin-left: 40px; }

  .contact-line { display: flex; align-items: center; gap: 7px; position: absolute; font-size: 13px; font-weight: 600; }
  .contact-line svg { width: 13px; height: 13px; flex: none; }
  .contact-phone { left: 50px; top: 148px; color: var(--ink); }
  .contact-email { left: 282px; top: 256px; color: var(--card-white); }
  .contact-web { left: 282px; top: 276px; color: var(--card-white); }
</style>
</head>
<body>

<section class="card card-back" aria-label="Card reverse">
  <div class="brand">
    <span class="brand-square"></span>
    <span class="brand-name">87Merchant</span>
  </div>
  <p class="website">87merchant.com.au</p>
</section>

<section class="card card-front" aria-label="Card front">
  <svg class="swoosh" viewBox="0 0 540 310" preserveAspectRatio="none" aria-hidden="true">
    <path d="M0,218 C110,238 210,240 268,238 C330,236 320,150 395,140 C445,134 500,146 540,156"
          fill="none" stroke="var(--brand-blue)" stroke-width="9"/>
    <path d="M0,228 C110,248 210,250 268,248 C340,246 325,160 398,150 C448,144 500,156 540,166 L540,310 L0,310 Z"
          fill="var(--charcoal)"/>
  </svg>

  <div class="brand">
    <span class="brand-square"></span>
    <span class="brand-name">87Merchant</span>
  </div>

  <div class="person">
    <p class="person-name">Dean <span class="surname">Colley</span></p>
    <p class="person-title">Business Development Manager</p>
  </div>

  <p class="contact-line contact-phone">
    <svg viewBox="0 0 14 14" aria-hidden="true"><circle cx="7" cy="7" r="6.5" fill="var(--ink)"/><path d="M4.6,3.6 L6,3.6 L6.6,5.4 L5.7,6.1 C6.1,7 6.9,7.9 7.9,8.3 L8.6,7.4 L10.4,8 L10.4,9.4 C7,9.6 4.4,7 4.6,3.6 Z" fill="#fff"/></svg>
    +61 417 658 294
  </p>
  <p class="contact-line contact-email">
    <svg viewBox="0 0 14 14" aria-hidden="true"><circle cx="7" cy="7" r="6.5" fill="#fff"/><rect x="3.5" y="4.6" width="7" height="4.8" fill="none" stroke="var(--charcoal)" stroke-width="1"/><path d="M3.5,4.6 L7,7.4 L10.5,4.6" fill="none" stroke="var(--charcoal)" stroke-width="1"/></svg>
    dean.colley@87merchant.com.au
  </p>
  <p class="contact-line contact-web">
    <svg viewBox="0 0 14 14" aria-hidden="true"><circle cx="7" cy="7" r="6.5" fill="#fff"/><circle cx="7" cy="7" r="3.6" fill="none" stroke="var(--charcoal)" stroke-width="1"/><path d="M3.4,7 H10.6 M7,3.4 C5.5,5 5.5,9 7,10.6 M7,3.4 C8.5,5 8.5,9 7,10.6" fill="none" stroke="var(--charcoal)" stroke-width="0.8"/></svg>
    87merchant.com.au
  </p>
</section>

</body>
</html>
```